Home page design for a business selling commercial cleaning machines

We need a home page web design for a wholesale business selling commercial and industrial cleaning machines and spare parts. There is a huge range of products but we don't want the home page to be too cluttered and confusing.
- The design needs to be practical and functional - sharp corners, lots of white with just accents/splashes of the business colours.
- This is a link to their holding page which is very very basic - http://www.vornaspec.co.nz/ - use this to get the accent colours but please use lots and lots more WHITE in the home page design! There are no colour codes available.
- The attached HPID (home page design information) is in table boxes just to see placement of information. Information in orange text. Words to go on the design in black text.
- Expected standard of design examples:
http://brimalo-aquaforce.com/
http://brimalointernational.com/
http://tovesk.com/
http://www.mulfin.wb.gs/ (different industry)
- Only use Google fonts. Non-responsive. Width 1100pixels. Header height (without nav bar) 150-160 pixels.
- Will need a PSD of the chosen homepage design (CS5 compatible)

```html
<!DOCTYPE html>
<html lang="en">
<head>
<meta charset="utf-8">
<title>Vornaspec – Cleaning Machines</title>
<link href="https://fonts.googleapis.com/css2?family=Roboto:wght@300;400;500;700&display=swap" rel="stylesheet">
<style>
:root{
  --orange:#f26a1b;
  --dark:#333333;
  --darker:#2a2a2a;
  --text:#333;
  --muted:#888;
  --line:#dcdcdc;
  --white:#fff;
}
*{box-sizing:border-box;margin:0;padding:0}
html,body{width:1200px;height:2419px;overflow:hidden}
body{font-family:'Roboto',sans-serif;background:#fafafa;color:var(--text);position:relative}
.abs{position:absolute}

/* header */
.header{left:0;top:0;width:1200px;height:118px;background:var(--orange)}
.header-center{left:387px;top:0;width:371px;height:118px;background:var(--dark)}
.brand{left:92px;top:26px;font-size:34px;font-weight:700;color:var(--white);letter-spacing:1px;display:flex;align-items:center;gap:10px}
.brand .dot{width:14px;height:14px;background:var(--white)}
.brand-tag{left:92px;top:70px;width:300px;font-size:12.5px;line-height:16px;color:var(--white)}
.header-intro{left:412px;top:14px;width:330px;font-size:13.5px;line-height:17px;color:var(--white);text-align:center}
.search{left:403px;top:78px;display:flex}
.search input{width:196px;height:24px;border:0;background:#555;color:#aaa;font:12px 'Roboto',sans-serif;padding:0 10px}
.search button{width:82px;height:24px;border:0;background:var(--orange);color:var(--white);font:500 12px 'Roboto',sans-serif}
.contact{left:774px;width:330px;font-size:12.5px;color:var(--white);display:flex;align-items:center;gap:10px;padding-bottom:8px;border-bottom:1px solid rgba(255,255,255,.35)}
.contact svg{flex:none}
.contact u{margin-left:6px}

/* nav */
.nav{left:0;top:118px;width:1200px;height:43px;background:var(--white);border-bottom:1px solid var(--line)}
.nav ul{list-style:none;display:flex;position:absolute;left:82px;top:0;height:43px}
.nav li{font-size:13.5px;padding:0 10px;line-height:43px;border-right:1px solid var(--line)}
.nav li.active{color:var(--orange)}
.nav li:last-child{border-right:0}

/* hero */
.hero{left:0;top:161px;width:1200px;height:445px;background:linear-gradient(120deg,#4a4341 0%,#7d7573 40%,#9a938f 65%,#5d5857 100%)}
.hero-panel{left:645px;top:161px;width:555px;height:445px;background:rgba(40,40,40,.88);clip-path:polygon(18% 0,100% 0,100% 100%,0 100%)}
.why-title{left:740px;top:210px;font-size:25px;font-weight:500;color:var(--white);padding-bottom:10px;border-bottom:2px solid #666;width:320px}
.why-list{left:660px;top:283px;list-style:none;color:var(--white);font-size:13px}
.why-list li{display:flex;align-items:flex-start;gap:12px;height:27.5px}
.hero-title{left:92px;top:416px;width:523px;height:61px;background:rgba(255,255,255,.85);font-size:40px;font-weight:500;color:#333;padding-left:26px;line-height:61px}
.hero-sub{left:142px;top:490px;width:423px;height:42px;background:var(--orange);color:var(--white);font-size:20px;font-weight:500;text-align:center;line-height:42px}

/* section titles */
.section-title{left:92px;width:1016px;display:flex;align-items:center;gap:26px;font-size:24px;font-weight:500;white-space:nowrap}
.section-title::before,.section-title::after{content:"";flex:1;height:1px;background:var(--line)}

/* product grid */
.products{left:92px;top:744px;width:1016px;height:272px;background:var(--white);border:1px solid var(--line);display:flex}
.product{flex:1;border-right:1px solid var(--line);text-align:center;padding-top:24px}
.product:last-child{border-right:0}
.product h3{font-size:16px;font-weight:400}
.product .shot{width:120px;height:130px;margin:20px auto 22px;background:linear-gradient(160deg,#d8d8d8,#8a8a8a)}
.btn-ghost{display:inline-block;width:113px;height:28px;border:1px solid var(--line);color:#aaa;font-size:13px;line-height:26px;text-align:center}
.btn-ghost.on{background:var(--orange);border-color:var(--orange);color:var(--white)}

/* feature cards */
.card{top:1065px;width:306px;height:388px;background:var(--white);border:1px solid var(--line)}
.card .pic{height:179px;position:relative}
.card .label{position:absolute;color:var(--white);font-size:13px;text-shadow:0 0 2px #000;white-space:nowrap}
.card h3{margin:16px 17px 0;font-size:16px;font-weight:400;line-height:21px}
.card p{margin:20px 17px 0;font-size:12.5px;line-height:16px;color:#555}
.card .btn-ghost{position:absolute;right:17px;bottom:18px}

/* request form */
.request{left:92px;top:1502px;width:1016px;height:274px;background:var(--white);border:1px solid var(--line)}
.request h2{position:absolute;left:0;top:38px;width:100%;display:flex;align-items:center;gap:26px;padding:0 44px;font-size:25px;font-weight:500;white-space:nowrap}
.request h2::before,.request h2::after{content:"";flex:1;height:1px;background:var(--line)}
.request .lead{position:absolute;top:70px;width:100%;text-align:center;font-size:18px;color:#444}
.fields{position:absolute;left:26px;top:118px;display:flex;gap:9px}
.fields span{width:186px;height:30px;border:1px solid var(--line);font-size:12.5px;color:#aaa;padding:0 9px;line-height:28px}
.btn-solid{position:absolute;left:371px;top:196px;width:274px;height:41px;background:var(--orange);color:var(--white);font-size:18px;font-weight:500;text-align:center;line-height:41px}

/* brands */
.brands{left:92px;top:1889px;width:1016px;height:166px;background:var(--white);border:1px solid var(--line);display:grid;grid-template-columns:repeat(4,1fr);grid-template-rows:1fr 1fr}
.brands div{border-right:1px solid var(--line);border-bottom:1px solid var(--line);display:flex;align-items:center;justify-content:center;gap:8px;font-size:18px;font-weight:500;color:#555}
.brands div:nth-child(4n){border-right:0}
.brands div:nth-child(n+5){border-bottom:0}
.brands i{width:12px;height:12px;background:var(--orange)}

/* footer */
.footer{left:0;top:2103px;width:1200px;height:297px;background:var(--dark)}
.footer-bar{left:0;top:2400px;width:1200px;height:19px;background:var(--orange)}
.fcol{top:2135px;width:220px;color:#ccc}
.fcol h4{font-size:16px;font-weight:400;color:var(--white);padding-bottom:8px;border-bottom:1px solid #666}
.fcol ul{list-style:none;margin-top:22px}
.fcol li{font-size:12.5px;color:#8a8a8a;height:27.5px;display:flex;align-items:center;gap:10px}
.fcol li::before{content:"";width:5px;height:5px;border-radius:50%;background:#777}
.fcol p{margin-top:24px;font-size:12.5px;color:#8a8a8a}
.footer-map{left:927px;top:2240px;width:140px;height:70px;background:#555}
.footer-brand{left:938px;top:2340px;font-size:24px;font-weight:700;color:#666;letter-spacing:1px}
</style>
</head>
<body>

<header>
  <div class="abs header"></div>
  <div class="abs header-center"></div>
  <div class="abs brand">VORNASPEC<span class="dot"></span></div>
  <div class="abs brand-tag">Service &amp; supply of most makes and models of cleaning machines and spare parts</div>
  <div class="abs header-intro">Wholesale importer &amp; distributor of quality Italian industrial, commercial &amp; domestic cleaning machines &amp; accessories</div>
  <form class="abs search"><input value="Enter Your Keyword"><button type="button">Search</button></form>

  <div class="abs contact" style="top:12px">
    <svg width="16" height="18" viewBox="0 0 16 18"><path d="M8 1a6 6 0 0 0-6 6c0 4.5 6 10 6 10s6-5.5 6-10a6 6 0 0 0-6-6z" fill="none" stroke="#fff" stroke-width="1.5"/><circle cx="8" cy="7" r="2" fill="#fff"/></svg>
    <span>4 / 27 Tarewa Rd, Otarua (office)<u>Open to the Public</u></span>
  </div>
  <div class="abs contact" style="top:50px">
    <svg width="16" height="18" viewBox="0 0 16 18"><path d="M8 1C5 6 3 9 3 11.5a5 5 0 0 0 10 0C13 9 11 6 8 1z" fill="none" stroke="#fff" stroke-width="1.5"/></svg>
    <span>Head office Merrow Coast | Distributors NZ wide</span>
  </div>
  <div class="abs contact" style="top:88px;border-bottom:0">
    <svg width="16" height="16" viewBox="0 0 16 16"><path d="M2 4c0-1 1-2 2-2l2 3-1.5 1.5c1 2 2.5 3.5 4.5 4.5L10.5 9.5l3 2c0 1-1 2-2 2C6 13.5 2 9.5 2 4z" fill="#fff"/></svg>
    <span>04 555 0187</span>
  </div>
</header>

<nav class="abs nav">
  <ul>
    <li class="active">Home</li><li>About</li><li>Water Blasters</li><li>Drain Cleaners</li><li>Customr Machines</li><li>Vacuum Cleaners</li><li>Pumps</li><li>Spare Parts</li><li>PTO Machines</li><li>FAQ</li><li>Quote</li><li>Contact</li>
  </ul>
</nav>

<section>
  <div class="abs hero" role="img" aria-label="Photo of an industrial vacuum cleaner on carpet"></div>
  <div class="abs hero-panel"></div>
  <h2 class="abs why-title">Why Choose Vornaspec?</h2>
  <ul class="abs why-list">
    <li style="margin-left:50px"><svg width="14" height="12" viewBox="0 0 14 12"><path d="M1 6l4 4 8-9" fill="none" stroke="#f26a1b" stroke-width="2"/></svg>High quality Italian cleaning machines</li>
    <li style="margin-left:44px"><svg width="14" height="12" viewBox="0 0 14 12"><path d="M1 6l4 4 8-9" fill="none" stroke="#f26a1b" stroke-width="2"/></svg>Wide range of brands and models</li>
    <li style="margin-left:38px"><svg width="14" height="12" viewBox="0 0 14 12"><path d="M1 6l4 4 8-9" fill="none" stroke="#f26a1b" stroke-width="2"/></svg>Specialist knowledge &amp; expert advice</li>
    <li style="margin-left:32px"><svg width="14" height="12" viewBox="0 0 14 12"><path d="M1 6l4 4 8-9" fill="none" stroke="#f26a1b" stroke-width="2"/></svg>Cost of machines – more affordable for top quality</li>
    <li style="margin-left:26px"><svg width="14" height="12" viewBox="0 0 14 12"><path d="M1 6l4 4 8-9" fill="none" stroke="#f26a1b" stroke-width="2"/></svg>Able to service and repair all types of cleaning machines</li>
    <li style="margin-left:20px"><svg width="14" height="12" viewBox="0 0 14 12"><path d="M1 6l4 4 8-9" fill="none" stroke="#f26a1b" stroke-width="2"/></svg>Huge range of affordable spare parts</li>
    <li style="margin-left:14px"><svg width="14" height="12" viewBox="0 0 14 12"><path d="M1 6l4 4 8-9" fill="none" stroke="#f26a1b" stroke-width="2"/></svg>Distributors nationwide offering excellent sales &amp; service support</li>
    <li style="margin-left:8px"><svg width="14" height="12" viewBox="0 0 14 12"><path d="M1 6l4 4 8-9" fill="none" stroke="#f26a1b" stroke-width="2"/></svg>Great family business with excellent customer service<br>for over 24 years!</li>
  </ul>
  <h1 class="abs hero-title">Hot High Pressure Washer</h1>
  <div class="abs hero-sub">Strong, Reliable, Great for Daily Use</div>
</section>

<h2 class="abs section-title" style="top:670px">Huge Rang of Quality Cleaning Machines</h2>
<div class="abs products">
  <div class="product"><h3>Water blasters</h3><div class="shot" role="img" aria-label="Water blaster machine"></div><span class="btn-ghost">View More</span></div>
  <div class="product"><h3>Drain cleaners</h3><div class="shot" role="img" aria-label="Red and yellow drain cleaner tanks" style="background:linear-gradient(90deg,#d93a2e,#e8c63a)"></div><span class="btn-ghost">View More</span></div>
  <div class="product"><h3>Custom Machines</h3><div class="shot" role="img" aria-label="Blue custom machine" style="background:linear-gradient(160deg,#6fa0d8,#2d5c9a)"></div><span class="btn-ghost">View More</span></div>
  <div class="product"><h3>Vacuum Cleaners</h3><div class="shot" role="img" aria-label="Yellow vacuum cleaner" style="background:linear-gradient(160deg,#f3cd2a,#444)"></div><span class="btn-ghost on">View More</span></div>
  <div class="product"><h3>Pumps high pres..</h3><div class="shot" role="img" aria-label="High pressure pump unit"></div><span class="btn-ghost">View More</span></div>
  <div class="product"><h3>PTO Machines</h3><div class="shot" role="img" aria-label="PTO machine"></div><span class="btn-ghost">View More</span></div>
</div>

<article class="abs card" style="left:92px">
  <div class="pic" role="img" aria-label="Photos of three cleaning machines" style="background:linear-gradient(135deg,#5a5a5a,#8a8a8a)">
    <span class="label" style="left:40px;top:148px">Aperta Plus</span>
    <span class="label" style="left:200px;top:58px">Facile</span>
    <span class="label" style="left:190px;top:148px">Convertor</span>
  </div>
  <h3>Huge Range of Quality Cleaning Machine</h3>
  <p>Browse the products, add any item to a quote requestform or give us a call for more informationNote sure what you need? Contact us for expert advice we're happy to assist</p>
  <span class="btn-ghost">All Products</span>
</article>
<article class="abs card" style="left:447px">
  <div class="pic" role="img" aria-label="Map of New Zealand" style="background:linear-gradient(135deg,#b9cad6,#cfc9b8)"></div>
  <h3>Nationwide Distributors for Sale<br>&amp; Services</h3>
  <p>Find out where your local distributor is – Vornaspec has a nationwide network of distributors you can contact direct. Fill in the form below or give us a call to find your local distributor.</p>
  <span class="btn-ghost">Contact</span>
</article>
<article class="abs card" style="left:802px">
  <div class="pic" role="img" aria-label="Photos of four spare parts" style="background:linear-gradient(135deg,#6a6a6a,#9a9a9a)">
    <span class="label" style="right:159px;top:70px">KPV.4410</span>
    <span class="label" style="right:8px;top:70px">RT.2085</span>
    <span class="label" style="right:159px;top:155px">KPV.3317</span>
    <span class="label" style="right:8px;top:155px">VM.LB240K4Q4Q</span>
  </div>
  <h3>Comprehensive Range of Spare Parts</h3>
  <p>Spare parts, servicing &amp; repairs – you want expert knowledge when it comes to any servicing and repairs needed. Vornaspec have a huge range of spare parts and the knowledge to fix virtually any machine.</p>
  <span class="btn-ghost">Spare Parts</span>
</article>

<section class="abs request">
  <h2>Would you like a Vornaspec representative to contact you?</h2>
  <div class="lead">Please fill in the form and we'll be in touch very soon…</div>
  <div class="fields"><span>First name.</span><span>Last name.</span><span>Contact phone.</span><span>Area you live in.</span><span>Any further details?</span></div>
  <div class="btn-solid">Subscribe</div>
</section>

<h2 class="abs section-title" style="top:1815px">Brands</h2>
<div class="abs brands">
  <div><i></i>Ostra Export</div>
  <div>Lumabase</div>
  <div>Clearfrost</div>
  <div>FALCOR</div>
  <div><i></i>Tessa</div>
  <div>Lumatech</div>
  <div>Gilda Riparo</div>
  <div>Gilda Riparo</div>
</div>

<footer>
  <div class="abs footer"></div>
  <div class="abs fcol" style="left:92px"><h4>Site link's</h4><ul><li>Home</li><li>About</li><li>Meet the Team</li><li>Testimonials</li><li>FAQ</li><li>Quote</li></ul></div>
  <div class="abs fcol" style="left:357px"><h4>Product</h4><ul><li>Hot water blasters</li><li>Cold water blasters electric</li><li>Cold water blasters petrol or</li><li>diesel</li><li>Steam water blasters</li><li></li></ul></div>
  <div class="abs fcol" style="left:622px"><h4>Key Markets</h4><ul><li>Custom machines</li><li>Vacuum Cleaners</li><li>Vacuum cleaners</li><li>Shampoo machines</li><li>Pumps high pressure</li><li>Spare Parts</li></ul></div>
  <div class="abs fcol" style="left:888px"><h4>Contact/Map</h4><p>4 / 27 Tarewa Rd, Otarua (office)</p></div>
  <div class="abs footer-map" role="img" aria-label="Small map of the office location"></div>
  <div class="abs footer-brand">VORNASPEC</div>
  <div class="abs footer-bar"></div>
</footer>

</body>
</html>
```